CD covers for a melodic death metal band from Quebec City, Canada *

We are a small band named "Ostrevik" and this is our first project with our own material. We plan to put our music on every platform available.Even though we know we are a small scale band, we are very proud of what we've done and we want the best covers possible to represent our work.This project consists of 2 album covers, part I and part II, but considered as a single project. We are really open to any design ideas but we really think that an album cover should represent the genre, the energy and the atmosphere of the music it presents. That's why we plan to release those albums one after the other separately, because they both have their own vibe. But to keep both parts as a whole entity, we thought of having the exact same image/representation/theme on both album covers, but with a different feel and ambiance for each of them.By keeping everything(logo, title, etc) at the same place, the emphasis of the covers should be in those differences. The Part I is more aggressive, fast tempo and "in your face". The Part II is more melodic, melancolic and dark. Our lyrical theme is oriented around the different flaws of humanity (Anger, Sorrow, Loneliness, Delusion). A lot of things that touches humanity. We put in attachments 2 song previews for each part, as reference. Note that these are not the final versions, as we are still in the recording/mixing process. We also put our logo, as we would like it to be present on both covers. You can adjust the background/border color as you see fit. We'd also like to have our name "Ostrevik" and "I" and "II" as album titles somewhere in the design, on any font/color you think is best.Thank you and we are very eager to see your ideas!

```html
<!DOCTYPE html>
<html lang="en">
<head>
<meta charset="utf-8">
<title>Ostrevik – Part I – Cover Presentation</title>
<link href="https://fonts.googleapis.com/css2?family=Montserrat:wght@400;600;700;800;900&display=swap" rel="stylesheet">
<style>
  :root {
    --bg: #000000;
    --header-strong: #8c8c8c;
    --header-soft: #7a7a7a;
    --label: #4a4a4a;
    --ink: #ffffff;
    --logo-stone: #c4bfb8;
    --storm-top: #2a2724;
    --storm-mid: #3b3733;
    --horizon: #4a4540;
    --ground: #231f1b;
    --ground-deep: #17140f;
    --fire-core: #ff7a2a;
    --fire-hot: #e0300c;
    --fire-deep: #8a1204;
    --stone-dark: #2b2522;
  }
  * { margin: 0; padding: 0; box-sizing: border-box; }
  html, body {
    width: 1200px; height: 1200px; overflow: hidden;
    background: var(--bg);
    font-family: "Montserrat", Arial, sans-serif;
  }
  .canvas { position: relative; width: 1200px; height: 1200px; }

  .sheet-title {
    position: absolute; left: 42px; top: 70px;
    font-size: 19px; letter-spacing: -0.2px; color: var(--header-strong);
  }
  .sheet-title strong { font-weight: 700; }
  .sheet-title span { font-weight: 400; color: var(--header-soft); font-size: 17px; }

  .sheet-label {
    position: absolute; left: 42px; top: 212px;
    transform: rotate(-90deg); transform-origin: left top;
    font-size: 13px; color: var(--label); font-weight: 400;
  }

  .cover {
    position: absolute; top: 326px; width: 550px; height: 548px; overflow: hidden;
  }
  .cover--back { left: 43px; }
  .cover--front { left: 606px; }

  .cover__scene {
    position: absolute; inset: 0;
    background:
      radial-gradient(ellipse 300px 90px at 35% 22%, rgba(120,112,100,0.35), rgba(0,0,0,0) 100%),
      linear-gradient(180deg, var(--storm-top) 0%, var(--storm-mid) 28%, #1c1a18 58%, var(--horizon) 66%, var(--ground) 72%, var(--ground-deep) 100%);
  }
  .cover--front .cover__scene {
    background:
      radial-gradient(ellipse 260px 90px at 60% 28%, rgba(120,112,100,0.3), rgba(0,0,0,0) 100%),
      linear-gradient(180deg, var(--storm-top) 0%, var(--storm-mid) 28%, #1c1a18 58%, var(--horizon) 68%, var(--ground) 74%, var(--ground-deep) 100%);
  }

  .cover__emblem {
    position: absolute; left: 96px; top: 170px; width: 364px; height: 330px;
    border-radius: 48%;
    background:
      radial-gradient(ellipse 70px 120px at 50% 48%, var(--stone-dark) 0%, rgba(43,37,34,0.85) 50%, rgba(43,37,34,0) 100%),
      radial-gradient(ellipse 110px 150px at 50% 50%, var(--fire-core) 0%, var(--fire-hot) 45%, rgba(138,18,4,0) 100%),
      radial-gradient(ellipse 182px 165px at 50% 50%, rgba(224,48,12,0.75) 0%, rgba(138,18,4,0.45) 60%, rgba(0,0,0,0) 100%);
    filter: saturate(1.2);
  }
  .cover__ground-shadow {
    position: absolute; left: 150px; top: 520px; width: 400px; height: 40px;
    background: radial-gradient(ellipse at 50% 50%, rgba(0,0,0,0.6), rgba(0,0,0,0) 70%);
  }

  .tracklist {
    position: absolute; left: 0; right: 0; top: 92px;
    text-align: center; color: var(--ink); font-size: 8.5px; font-weight: 400;
    letter-spacing: 0.6px; line-height: 15px;
  }
  .tracklist__heading { font-size: 10.5px; letter-spacing: 1px; margin-bottom: 10px; }
  .tracklist__more { font-weight: 700; margin-top: 2px; }

  .wordmark { position: absolute; text-align: center; color: var(--ink); font-weight: 800; }
  .wordmark__name { display: block; line-height: 1; }
  .wordmark__part { display: block; font-weight: 600; }

  .cover--back .wordmark { left: 0; right: 0; top: 474px; }
  .cover--back .wordmark__name { font-size: 27px; letter-spacing: -0.5px; }
  .cover--back .wordmark__part { font-size: 7px; letter-spacing: 3px; margin-top: 2px; }

  .cover__title {
    position: absolute; left: 0; right: 0; top: 22px; text-align: center;
    font-weight: 900; font-size: 106px; line-height: 1; letter-spacing: -3px;
    color: var(--logo-stone);
  }

  .spine {
    position: absolute; left: 596px; top: 848px;
    transform: rotate(-90deg); transform-origin: left top;
    font-size: 6px; font-weight: 700; letter-spacing: 1.6px; color: var(--ink);
    white-space: nowrap;
  }

  .release-mark { left: 0; right: 0; top: 1046px; }
  .release-mark .wordmark__name { font-size: 52px; letter-spacing: -1px; }
  .release-mark .wordmark__part { font-size: 11px; letter-spacing: 5px; margin-top: 4px; }
</style>
</head>
<body>
<main class="canvas">
  <h1 class="sheet-title"><strong>OSTREVIK</strong> <span>_ PART I</span></h1>
  <div class="sheet-label">Cover_001</div>

  <section class="cover cover--back" aria-label="Back cover">
    <div class="cover__scene" role="img" aria-label="Stormy dark sky over a barren cracked desert plain"></div>
    <div class="tracklist">
      <p class="tracklist__heading">XXX XXXXXX XXXXX</p>
      <p>01. XXXX XXXXXX XX</p>
      <p>02. XXXXXX XXXXXXXX XXXXX</p>
      <p>03. XXX XXXXX XX XXXXX</p>
      <p>04. XXXXXXX XXX</p>
      <p>05. XXXXX XX XXXXX X</p>
      <p class="tracklist__more">...</p>
    </div>
    <div class="wordmark">
      <span class="wordmark__name">Ostrevik</span>
      <span class="wordmark__part">PART I</span>
    </div>
  </section>

  <div class="spine">OSTREVIK _ PART I</div>

  <section class="cover cover--front" aria-label="Front cover">
    <div class="cover__scene" role="img" aria-label="Stormy sky over a barren cracked desert plain"></div>
    <div class="cover__ground-shadow"></div>
    <div class="cover__emblem" role="img" aria-label="Massive stone cross engulfed in fierce red and orange flames"></div>
    <div class="cover__title">Ostrevik</div>
  </section>

  <div class="wordmark release-mark">
    <span class="wordmark__name">Ostrevik</span>
    <span class="wordmark__part">PART I</span>
  </div>
</main>
</body>
</html>
```